Business Card New Design for Corvella

We would like a new look on our business card, using the same style, the same colors blue, gray and white with similar font that is represented on the new Sell Sheet. We recently re-designed our Sell Sheets - I've attached a sell sheet file for your reference. I've also attached our current business card and our logo. Keep the same information listed on each side of the card.

Contact Information for Business Card

Use details given on example provided

Font styles to use
Other font styles liked:
• Myriad Regular and Bold

Colors

Designer to choose colors to be used in the design.

Requirements
Must have
• Current Information that was provided on the current business card. Colors Must use Blue, Gray and White, the same colors as the sell sheet example.

```html
<!DOCTYPE html>
<html lang="en">
<head>
<meta charset="utf-8">
<title>Corvella Business Card</title>
<link href="https://fonts.googleapis.com/css2?family=Michroma&family=Montserrat:wght@700;800&family=Work+Sans:wght@400;600&display=swap" rel="stylesheet">
<style>
  :root {
    --brand-blue: #2e3898;
    --brand-gray: #3c3c3e;
    --card-white: #ffffff;
    --backdrop: #d9d9dc;
  }
  html, body {
    margin: 0;
    width: 1200px;
    height: 900px;
    overflow: hidden;
    background: var(--backdrop);
  }
  .canvas {
    position: relative;
    width: 1200px;
    height: 900px;
  }
  .card {
    position: absolute;
    width: 560px;
    height: 320px;
    border-radius: 18px;
    overflow: hidden;
    box-shadow: 0 10px 28px rgba(0,0,0,0.18);
  }
  .card-back {
    left: 600px;
    top: 110px;
    background: var(--brand-blue);
    color: var(--card-white);
    display: flex;
    align-items: center;
    justify-content: center;
  }
  .product-list {
    list-style: none;
    margin: 0;
    padding: 0;
    text-align: center;
    font-family: "Michroma", sans-serif;
    font-size: 14px;
    line-height: 24px;
    letter-spacing: 1.5px;
    text-transform: uppercase;
  }
  .card-front {
    left: 40px;
    top: 470px;
    background: var(--card-white);
  }
  .front-wave {
    position: absolute;
    inset: 0;
  }
  .company-name {
    position: absolute;
    left: 34px;
    top: 68px;
    margin: 0;
    font-family: "Work Sans", sans-serif;
    font-weight: 600;
    font-size: 14px;
    color: var(--brand-blue);
  }
  .address {
    position: absolute;
    left: 34px;
    top: 92px;
    margin: 0;
    font-family: "Work Sans", sans-serif;
    font-size: 14px;
    line-height: 18px;
    letter-spacing: 1px;
    color: var(--brand-gray);
    font-style: normal;
  }
  .contact-list {
    position: absolute;
    left: 20px;
    top: 134px;
    margin: 0;
    padding: 0;
    list-style: none;
    font-family: "Work Sans", sans-serif;
    font-size: 14px;
    line-height: 20px;
    letter-spacing: 1px;
    color: var(--brand-gray);
  }
  .contact-list li {
    display: flex;
    align-items: center;
    gap: 6px;
  }
  .contact-icon {
    width: 14px;
    height: 14px;
    flex: none;
  }
  .person {
    position: absolute;
    right: 22px;
    top: 56px;
    text-align: right;
    color: var(--card-white);
  }
  .person-name {
    margin: 0;
    font-family: "Montserrat", sans-serif;
    font-weight: 800;
    font-size: 26px;
    letter-spacing: 3px;
    line-height: 30px;
  }
  .person-title {
    margin: 0;
    font-family: "Work Sans", sans-serif;
    font-size: 15px;
    letter-spacing: 1px;
  }
  .wordmark {
    position: absolute;
    left: 220px;
    top: 252px;
    margin: 0;
    font-family: "Work Sans", sans-serif;
    font-weight: 400;
    font-size: 38px;
    letter-spacing: 6px;
    color: var(--brand-gray);
  }
</style>
</head>
<body>
<main class="canvas">

  <section class="card card-back" aria-label="Card back">
    <ul class="product-list">
      <li>Conveyyors</li>
      <li>Target Sauce Applicators</li>
      <li>Targertopping Applicators</li>
      <li>Waterfall Toppng Applicators</li>
      <li>Pepeeroni / Meat Sliger / Apllicators</li>
      <li>Portion Controlled Filler Pimps</li>
      <li>Dry Ingredient Applicators</li>
      <li>Check Weigh Conveyors</li>
      <li>Portion Compensators</li>
    </ul>
  </section>

  <section class="card card-front" aria-label="Card front">
    <svg class="front-wave" viewBox="0 0 560 320" width="560" height="320" aria-hidden="true">
      <path d="M0,0 H560 V238 C500,228 450,212 400,185 C340,150 330,90 290,60 C240,24 120,22 0,28 Z" fill="var(--brand-blue)"/>
      <path d="M0,20 C120,14 240,16 290,52 C330,82 340,142 400,177 C450,204 500,220 560,230" fill="none" stroke="var(--brand-gray)" stroke-width="7" transform="translate(0,-2)"/>
    </svg>

    <p class="company-name">Corvella Technical services, inc.</p>
    <address class="address">4180 Ridgeline road<br>alder park, IL 60917</address>

    <ul class="contact-list">
      <li>
        <svg class="contact-icon" viewBox="0 0 14 14"><rect width="14" height="14" rx="3" fill="var(--brand-blue)"/><path d="M4.5,3 L6,4.5 L5,6 C5.6,7.3 6.7,8.4 8,9 L9.5,8 L11,9.5 L10,11 C6.5,10.6 3.4,7.5 3,4 Z" fill="#fff"/></svg>
        (555)203-1948
      </li>
      <li>
        <svg class="contact-icon" viewBox="0 0 14 14"><rect width="14" height="14" rx="3" fill="var(--brand-blue)"/><rect x="4.5" y="2.5" width="5" height="9" rx="1" fill="none" stroke="#fff" stroke-width="1.2"/></svg>
        (555) 203-7614
      </li>
      <li>
        <svg class="contact-icon" viewBox="0 0 14 14"><rect width="14" height="14" rx="3" fill="var(--brand-blue)"/><rect x="3" y="6" width="8" height="5" rx="1" fill="#fff"/><path d="M3,6 C3,3 11,3 11,6" fill="none" stroke="#fff" stroke-width="1.2"/></svg>
        (555) 318-2070
      </li>
      <li>
        <svg class="contact-icon" viewBox="0 0 14 14"><rect width="14" height="14" rx="3" fill="var(--brand-blue)"/><rect x="3" y="5" width="8" height="6" fill="#fff"/><rect x="4.5" y="2.5" width="5" height="3" fill="none" stroke="#fff" stroke-width="1"/></svg>
        (555) 203-1948 x 114
      </li>
      <li>
        <svg class="contact-icon" viewBox="0 0 14 14"><rect width="14" height="14" rx="3" fill="var(--brand-blue)"/><rect x="2.5" y="4" width="9" height="6.5" fill="none" stroke="#fff" stroke-width="1.1"/><path d="M2.5,4 L7,8 L11.5,4" fill="none" stroke="#fff" stroke-width="1.1"/></svg>
        mhale@c-t-s.com
      </li>
    </ul>

    <div class="person">
      <p class="person-name">MARCUS HALE</p>
      <p class="person-title">CEO</p>
    </div>

    <p class="wordmark">CORVELLA</p>
  </section>

</main>
</body>
</html>
```